BRENLO CAPITAL INSTITUTIONAL PRESENTATION

To create a powerpoint presentation with selected art and text.
Target Market(s)
Potential Investors for the fund
Industry/Entity Type
Finance
Font styles to use
Sans Serif
Colors
0692cd
0255a3
Requirements
Must have
- Unique art, to look sober and professional
Nice to have
- Modern look
Should not have
- Red as color...

```html
<!DOCTYPE html>
<html lang="en">
<head>
<meta charset="utf-8">
<title>Brenlo Capital – Macro Global Fund</title>
<link href="https://fonts.googleapis.com/css2?family=Source+Sans+3:wght@400;700&display=swap" rel="stylesheet">
<style>
:root{
  --blue:#0692cd;
  --navy:#0255a3;
  --sky:#cfe7f5;
  --grey:#8a8a8a;
  --light-grey:#c9c9c9;
  --ink:#333;
  --line:#9a9a9a;
  --font:"Source Sans 3",Arial,sans-serif;
}
*{box-sizing:border-box;margin:0;padding:0}
html,body{width:1200px;height:1001px;overflow:hidden;background:#fff;font-family:var(--font);color:var(--ink)}
.deck{position:relative;width:1200px;height:1001px}
.slide{position:absolute;width:272px;height:153px;background:#fff;border:1px solid var(--line);overflow:hidden}
.c1{left:0}.c2{left:300px}.c3{left:600px}.c4{left:900px}
.r1{top:0}.r2{top:165px}.r3{top:330px}.r4{top:495px}.r5{top:660px}.r6{top:825px}
.title{position:absolute;left:18px;top:12px;font-size:8px;font-weight:700;color:var(--blue)}
.subtitle{position:absolute;left:18px;top:24px;font-size:4.4px;font-weight:700;color:var(--ink)}
.body{position:absolute;left:18px;font-size:2.9px;line-height:4.2px;color:var(--ink)}
.body li{margin-left:4px}
.body .head{color:var(--blue);font-weight:700}
.page{position:absolute;bottom:6px;left:0;right:0;text-align:center;font-size:2.6px;color:var(--grey)}
.brand{position:absolute;bottom:5px;right:10px;font-size:3.4px;font-weight:700;color:var(--ink);display:flex;align-items:center;gap:2px}
.brand i{display:block;width:4px;height:4px;border-radius:50%;background:var(--navy)}
.box{position:absolute;font-size:2.7px;line-height:3.4px;color:#fff;display:flex;align-items:center;justify-content:center;text-align:center;padding:2px}
.b-blue{background:var(--blue)}.b-navy{background:var(--navy)}.b-grey{background:var(--light-grey);color:var(--ink)}.b-dgrey{background:#7b7b7b}.b-sky{background:var(--sky);color:var(--ink)}
svg{position:absolute;left:0;top:0}
svg text{font-family:var(--font)}
.cover-art{position:absolute;left:0;top:0;width:272px;height:153px;background:linear-gradient(155deg,#cfe7f5 0%,#dcdcdc 28%,#eef6fb 45%,#fff 62%)}
</style>
</head>
<body>
<div class="deck">

<!-- Cover -->
<section class="slide c1 r1">
  <div class="cover-art" role="img" aria-label="Abstract cover artwork in soft blue and grey tones"></div>
  <div style="position:absolute;left:183px;top:99px;font-size:8.5px;font-weight:700;color:var(--blue)">Macro Global Fund</div>
  <div style="position:absolute;left:184px;top:114px;font-size:6px;font-weight:700;color:var(--navy);display:flex;align-items:center;gap:3px"><i style="display:block;width:6px;height:6px;border-radius:50%;background:var(--navy)"></i>BRENLO CAPITAL</div>
  <div style="position:absolute;left:216px;top:127px;font-size:3px;color:var(--blue)">JANUARY 2018</div>
</section>

<!-- Table of contents -->
<section class="slide c2 r1">
  <div class="title">Table of Contents</div>
  <div class="body" style="top:33px;width:236px;font-size:2.7px;line-height:4px">
    <div style="display:grid;grid-template-columns:1fr auto">
      <span>Executive Summary</span><span>3</span>
      <span>The Opportunity</span><span>4</span>
      <span>Brenlo Capital: Introduction</span><span>5</span>
      <span>A Leading Independent Asset Manager</span><span>6</span>
      <span>Brenlo Capital: Tomas Varel – CIO and Founding Partner</span><span>7</span>
      <span>Brenlo Capital: A unique and proven approach</span><span>8</span>
      <span>Philosophy and investments process</span><span>9</span>
      <span>Brenlo Macro Global Fund – The Opportunity</span><span>10</span>
      <span>Brenlo Capital – A unique investment model</span><span>11</span>
      <span>Brenlo Macro Global Fund – Trade Ideas 1</span><span>12</span>
      <span>Brenlo Macro Global Fund – Trade Ideas 2</span><span>13</span>
      <span>Portfolio Construction: Low correlation positions</span><span>14</span>
      <span>Performance Chart (Brenlo Macro 77)</span><span>15</span>
      <span>Consistent Returns</span><span>16</span>
      <span>Key Facts – Brenlo Macro Global Fund</span><span>17</span>
      <span>Flagship Funds</span><span>18</span>
      <span>Flagship Funds Performance</span><span>19</span>
      <span>The Team</span><span>20</span>
      <span>Disclosures</span><span>21</span>
      <span>Contact information</span><span>22</span>
    </div>
  </div>
  <div class="page">2</div><div class="brand"><i></i>BRENLO CAPITAL</div>
</section>

<!-- Executive summary -->
<section class="slide c3 r1">
  <div class="title">Executive Summary</div>
  <ul class="body" style="top:33px"><li>Text</li><li>Text</li><li>Text</li><li>Text</li></ul>
  <div class="page">3</div><div class="brand"><i></i>BRENLO CAPITAL</div>
</section>

<!-- The opportunity -->
<section class="slide c4 r1">
  <div class="title">The Opportunity</div>
  <div class="body" style="top:33px;width:240px">
    <div class="head">Brazil</div>
    <ul><li>Rates remain attractive over a one-year view</li><li>Fiscal outlook drives curve and currency moves</li><li>Select opportunities in listed equities and FX</li></ul>
    <div class="head" style="margin-top:4px">Other EMs</div>
    <ul><li>A slower Fed path favours emerging-market carry positions</li><li>Valuations in EM local debt remain broadly cheap</li><li>Risk of contagion is low versus previous cycles; relative value trades selected</li></ul>
  </div>
  <div class="page">4</div><div class="brand"><i></i>BRENLO CAPITAL</div>
</section>

<!-- Intro -->
<section class="slide c1 r2">
  <div class="title">Brenlo Capital</div>
  <div class="subtitle">Introduction</div>
  <ul class="body" style="top:34px;width:240px">
    <li>Founded in 2010, Brenlo Capital is an independent asset manager focused on the generation of superior returns.</li>
    <li>Investment decisions are fundamental and macro-driven, with disciplined risk control and portfolio positioning.</li>
    <li>Expertise in management of FX, interest rate and equity strategies, both in Brazil and globally.</li>
    <li>Brenlo Capital has the largest inflows of any hedge fund house in the region since 2014.</li>
  </ul>
  <div class="body" style="top:76px;font-size:2.2px;color:var(--grey)">Source: Brenlo Capital</div>
  <div class="page">5</div><div class="brand"><i></i>BRENLO CAPITAL</div>
</section>

<!-- Leading asset manager -->
<section class="slide c2 r2">
  <div class="title">A Leading Independent Asset Manager</div>
  <div class="body" style="top:32px;color:var(--blue)">Brenlo Capital: AUM<br><span style="color:var(--grey)">R$ billion</span></div>
  <svg width="272" height="153" viewBox="0 0 272 153">
    <g transform="translate(70 85)">
      <circle r="26" fill="none" stroke="#cfe7f5" stroke-width="14"/>
      <circle r="26" fill="none" stroke="#0255a3" stroke-width="14" stroke-dasharray="40 200" transform="rotate(-90)"/>
      <circle r="26" fill="none" stroke="#8a8a8a" stroke-width="14" stroke-dasharray="12 200" stroke-dashoffset="-40" transform="rotate(-90)"/>
      <circle r="26" fill="none" stroke="#0692cd" stroke-width="14" stroke-dasharray="10 200" stroke-dashoffset="-52" transform="rotate(-90)"/>
    </g>
    <g font-size="2.4" fill="#333">
      <text x="56" y="52">Brenlo Macro Strategy</text><text x="92" y="60">Brenlo Prev</text>
      <text x="22" y="63">Brenlo Macro Global</text><text x="30" y="69">Brenlo Strat</text>
      <text x="104" y="77">Brenlo Advanced</text><text x="62" y="118">Brenlo Macro</text>
    </g>
  </svg>
  <div class="box b-navy" style="left:138px;top:50px;width:55px;height:13px">BRENLO / STRATEGY</div>
  <div class="box b-navy" style="left:198px;top:50px;width:55px;height:13px">R$ 2.0 B</div>
  <div class="box b-grey" style="left:138px;top:68px;width:55px;height:13px">BRENLO / PREV</div>
  <div class="box b-grey" style="left:198px;top:68px;width:55px;height:13px">R$ 2.1 B</div>
  <div class="box b-sky" style="left:138px;top:86px;width:55px;height:13px">BRENLO / MACRO Global</div>
  <div class="box b-sky" style="left:198px;top:86px;width:55px;height:13px">R$ 1.2 B</div>
  <div class="box b-blue" style="left:138px;top:104px;width:55px;height:13px">BRENLO / ADVANCED Global</div>
  <div class="box b-blue" style="left:198px;top:104px;width:55px;height:13px">R$ 4.0 B</div>
  <div class="body" style="top:130px;font-size:2.2px;line-height:3px;color:var(--grey)">Approximate AUM as of Dec 2017<br>Source: Brenlo Capital</div>
  <div class="page">6</div><div class="brand"><i></i>BRENLO CAPITAL</div>
</section>

<!-- Founding partner -->
<section class="slide c3 r2">
  <div class="title">Brenlo Capital</div>
  <div class="subtitle">Tomas Varel – CIO and Founding Partner</div>
  <div class="body" style="top:34px;font-size:2.4px">Successful experience with a strong track record of performance</div>
  <svg width="272" height="153" viewBox="0 0 272 153">
    <line x1="30" y1="52" x2="245" y2="52" stroke="#0692cd" stroke-width="0.8"/>
    <g fill="#0692cd"><circle cx="30" cy="52" r="1.5"/><circle cx="130" cy="52" r="1.5"/><circle cx="230" cy="52" r="1.5"/><circle cx="243" cy="52" r="1.5"/></g>
    <g stroke="#0692cd" stroke-width="0.4"><line x1="30" y1="52" x2="30" y2="58"/><line x1="130" y1="52" x2="130" y2="58"/><line x1="230" y1="52" x2="230" y2="76"/></g>
    <g font-size="2.3" fill="#555">
      <text x="27" y="48">1999</text><text x="127" y="48">2005</text><text x="224" y="48">2010</text><text x="239" y="48">2018</text>
    </g>
  </svg>
  <div class="body" style="top:58px;left:30px;width:85px;font-size:2.3px;line-height:3.2px;color:var(--grey);text-align:center">Head of Proprietary Trading at a regional bank – top decile in yearly performance</div>
  <div class="body" style="top:58px;left:130px;width:90px;font-size:2.3px;line-height:3.2px;color:var(--grey);text-align:center">Head of Macro Asset Management – top decile in yearly performance across all funds</div>
  <div class="body" style="top:78px;left:200px;width:62px;font-size:2.3px;line-height:3.2px;color:var(--grey);text-align:center">Founded Brenlo Capital – multi-strategy funds and all investment decisions</div>
  <div class="page">7</div><div class="brand"><i></i>BRENLO CAPITAL</div>
</section>

<!-- Unique approach -->
<section class="slide c4 r2">
  <div class="title">Brenlo Capital</div>
  <div class="subtitle">A unique and proven approach</div>
  <ul class="body" style="top:34px;width:240px">
    <li>Proven label generation through position structuring</li>
    <li>Balanced approach allows scalability in the decision process</li>
    <li>Low exposure with positions that limit drawdown and return volatility under stress</li>
    <li>Academic grounding of a negative correlation that limits risk across the portfolio</li>
    <li>A global team with expertise in both developed and emerging markets, especially Brazil</li>
    <li>Alpha: more than 8% annualized and 70% of days without material losses</li>
  </ul>
  <div class="page">8</div><div class="brand"><i></i>BRENLO CAPITAL</div>
</section>

<!-- Philosophy -->
<section class="slide c1 r3">
  <div class="title">Philosophy and investments process</div>
  <svg width="272" height="153" viewBox="0 0 272 153">
    <g font-size="2.6">
      <rect x="18" y="35" width="10" height="6" fill="#0692cd"/><text x="21" y="39.5" fill="#fff">1</text>
      <rect x="102" y="35" width="10" height="6" fill="#c9c9c9"/><text x="105" y="39.5" fill="#333">2</text>
      <rect x="186" y="35" width="10" height="6" fill="#0255a3"/><text x="189" y="39.5" fill="#fff">3</text>
      <path d="M18 45 H94 L98 49 L94 53 H18 Z" fill="#0692cd"/><text x="21" y="50" fill="#fff">Identifying trends</text>
      <path d="M102 45 H175 L179 49 L175 53 H102 Z" fill="#c9c9c9"/><text x="105" y="50" fill="#333">Trend search</text>
      <rect x="186" y="45" width="68" height="8" fill="#0255a3"/><text x="189" y="50" fill="#fff">Portfolio Construction</text>
    </g>
  </svg>
  <div class="box b-blue" style="left:18px;top:57px;width:76px;height:32px">Brenlo's investment team identify long term trends and anticipate capital flows in time</div>
  <div class="box b-grey" style="left:102px;top:57px;width:73px;height:32px">Each opportunity undergoes a wide range of stress scenarios and fundamental analysis</div>
  <div class="box b-navy" style="left:186px;top:57px;width:68px;height:32px">Balance the portfolio efficiently between return and volatility</div>
  <div class="body" style="top:91px;font-size:2.4px">Macro sources illustration</div>
  <div class="box b-blue" style="left:18px;top:98px;width:76px;height:7px;justify-content:flex-start">Global producer flows</div>
  <div class="box b-blue" style="left:18px;top:107px;width:76px;height:7px;justify-content:flex-start">Intellectual property</div>
  <div class="box b-blue" style="left:18px;top:116px;width:76px;height:7px;justify-content:flex-start">Scale of production</div>
  <div class="box b-grey" style="left:102px;top:98px;width:73px;height:7px;justify-content:flex-start">US fixed income</div>
  <div class="box b-grey" style="left:102px;top:107px;width:73px;height:7px;justify-content:flex-start">Tech platforms</div>
  <div class="box b-grey" style="left:102px;top:116px;width:73px;height:7px;justify-content:flex-start">Index futures</div>
  <div class="box b-navy" style="left:186px;top:98px;width:56px;height:25px">Mix of low-correlation trades allowing the portfolio to perform across scenarios</div>
  <div class="box b-navy" style="left:244px;top:98px;width:10px;height:25px;writing-mode:vertical-rl">Risk</div>
  <div class="page">9</div><div class="brand"><i></i>BRENLO CAPITAL</div>
</section>

<!-- Fund opportunity -->
<section class="slide c2 r3">
  <div class="title">Brenlo Macro Global Fund</div>
  <div class="subtitle">The Opportunity</div>
  <ul class="body" style="top:34px;width:240px">
    <li>Take your offshore capital to Brenlo Capital's fund which has a proven track record</li>
    <li>Exposure to a range of FX markets</li>
    <li>Volatility of the main asset is limited</li>
    <li>Portfolios are constructed with a deep understanding of emerging markets</li>
    <li>A track record of ten years; Brenlo Capital has proven depth in the asset class</li>
    <li>In relative terms the fund ranks in the top quartile of managers in the region</li>
  </ul>
  <div class="page">10</div><div class="brand"><i></i>BRENLO CAPITAL</div>
</section>

<!-- Investment model -->
<section class="slide c3 r3">
  <div class="title">Brenlo Capital</div>
  <div class="subtitle">A unique investment model</div>
  <svg width="272" height="153" viewBox="0 0 272 153">
    <g transform="translate(136 86)">
      <path d="M0 -42 A42 42 0 0 1 36 -21 L22 -13 A26 26 0 0 0 0 -26 Z" fill="#c9c9c9"/>
      <path d="M36 -21 A42 42 0 0 1 36 21 L22 13 A26 26 0 0 0 22 -13 Z" fill="#0692cd"/>
      <path d="M36 21 A42 42 0 0 1 0 42 L0 26 A26 26 0 0 0 22 13 Z" fill="#8a8a8a"/>
      <path d="M0 42 A42 42 0 0 1 -36 21 L-22 13 A26 26 0 0 0 0 26 Z" fill="#0255a3"/>
      <path d="M-36 21 A42 42 0 0 1 -36 -21 L-22 -13 A26 26 0 0 0 -22 13 Z" fill="#0255a3"/>
      <path d="M-36 -21 A42 42 0 0 1 0 -42 L0 -26 A26 26 0 0 0 -22 -13 Z" fill="#0692cd"/>
      <circle r="22" fill="#0255a3"/>
      <g font-size="2.6" fill="#fff" text-anchor="middle">
        <text y="-3">Seek Returns</text><text y="1">Global</text><text y="5">Portfolio</text>
        <text x="-14" y="-31">1. Long term</text><text x="16" y="-31">2. Tested</text>
        <text x="31" y="1">3. Global</text><text x="14" y="35">4. Structured</text>
        <text x="-14" y="35">5. Low Corr.</text><text x="-31" y="1">6. Risk</text>
      </g>
    </g>
  </svg>
  <div class="box b-dgrey" style="left:18px;top:40px;width:58px;height:18px">Investment themes with long-term horizon</div>
  <div class="box b-dgrey" style="left:18px;top:72px;width:58px;height:16px">Diversification in macro assets</div>
  <div class="box b-dgrey" style="left:18px;top:102px;width:58px;height:16px">Investments with low correlation</div>
  <div class="box b-dgrey" style="left:196px;top:40px;width:58px;height:18px">Structured trades and disciplined risk</div>
  <div class="box b-dgrey" style="left:196px;top:72px;width:58px;height:16px">Global view with emerging focus</div>
  <div class="box b-dgrey" style="left:196px;top:102px;width:58px;height:16px">Consistent returns across cycles</div>
  <div class="page">11</div><div class="brand"><i></i>BRENLO CAPITAL</div>
</section>

<!-- Trade ideas 1 -->
<section class="slide c4 r3">
  <div class="title">Brenlo Macro Global Fund</div>
  <div class="subtitle">Trade Ideas — 1</div>
  <div class="body" style="top:34px;width:240px">
    <div class="head">Trade Description — An investment theme that sets front-lines</div>
    <ul><li>Long US rate curve</li><li>Build on a clear reflation narrative in the major economies</li><li>Hedge with short positions in growth-sensitive currencies</li></ul>
    <div class="head" style="margin-top:3px">Instruments — Constructing a global macro trade</div>
    <ul><li>Select rates, currency and index futures for liquidity</li><li>Size each leg for the expected volatility and drawdown</li><li>Review correlation with existing book positions weekly</li><li>Use options where payoff asymmetry is attractive</li><li>Monitor positioning and central bank communication</li></ul>
    <div class="head" style="margin-top:4px">Structured trade: one position has a negative correlation to the other, both with a positive expected return.</div>
  </div>
  <div class="page">12</div><div class="brand"><i></i>BRENLO CAPITAL</div>
</section>

<!-- Trade ideas 2 -->
<section class="slide c1 r4">
  <div class="title">Brenlo Macro Global Fund</div>
  <div class="subtitle">Trade Ideas — 2</div>
  <div class="body" style="top:34px;width:240px">
    <div class="head">FX Pair Trade – Short Yen and Long Brazil Real</div>
    <ul><li>Policy divergence between the two central banks supports carry</li><li>Brazil offers attractive real yields versus peers</li><li>Positioning is already light in the real</li><li>Exposure hedged with index options</li><li>Defined stop-loss and review levels</li><li>Expected to be negatively correlated with the rest of book</li></ul>
  </div>
  <div class="page">13</div><div class="brand"><i></i>BRENLO CAPITAL</div>
</section>

<!-- Portfolio construction -->
<section class="slide c2 r4">
  <div class="title">Portfolio Construction</div>
  <div class="subtitle">Low correlation positions that are also complementary</div>
  <div class="body" style="top:32px;color:var(--blue);font-size:2.4px">Illustration of the Portfolio construction</div>
  <div role="img" aria-label="Illustration of a portfolio cube of asset classes with country and company markers" style="position:absolute;left:18px;top:38px;width:236px;height:98px;background:radial-gradient(ellipse at center,#4fa9d8 0%,#cfe5f2 45%,#eef5fa 100%)"></div>
  <svg width="272" height="153" viewBox="0 0 272 153">
    <g font-size="2.3" fill="#333"><text x="21" y="43">Emerging country currencies</text><text x="222" y="43">Global equity shares</text><text x="30" y="123">Developed country currencies</text><text x="112" y="123">Commodities</text><text x="160" y="123">Global equity indexes</text></g>
    <g fill="#7b7b7b"><circle cx="30" cy="52" r="4"/><circle cx="30" cy="66" r="4"/><circle cx="30" cy="80" r="4"/><circle cx="30" cy="94" r="4"/><circle cx="236" cy="52" r="4"/><circle cx="236" cy="66" r="4"/><circle cx="236" cy="80" r="4"/><circle cx="236" cy="94" r="4"/><circle cx="40" cy="130" r="3"/><circle cx="55" cy="130" r="3"/><circle cx="118" cy="130" r="3"/><circle cx="178" cy="130" r="3"/><circle cx="198" cy="130" r="3"/></g>
    <text x="136" y="50" font-size="4" font-weight="700" fill="#0255a3" text-anchor="middle">BRENLO CAPITAL</text>
  </svg>
  <div class="page">14</div><div class="brand"><i></i>BRENLO CAPITAL</div>
</section>

<!-- Performance chart -->
<section class="slide c3 r4">
  <div class="title">Performance Chart</div>
  <div class="subtitle" style="font-weight:400">(Brenlo Macro 77)</div>
  <div class="page">15</div><div class="brand"><i></i>BRENLO CAPITAL</div>
</section>

<!-- Consistent returns -->
<section class="slide c4 r4">
  <div class="title">Consistent Returns</div>
  <div class="body" style="top:33px;color:var(--blue);font-size:2.5px;line-height:3.4px">6 Month Moving Average % Returns<br><span style="color:var(--grey)">207 investment windows, Brenlo Macro</span></div>
  <div class="body" style="top:33px;left:142px;color:var(--blue);font-size:2.5px;line-height:3.4px">12 Month Moving Average % Returns<br><span style="color:var(--grey)">195 investment windows, Brenlo Macro</span></div>
  <svg width="272" height="153" viewBox="0 0 272 153">
    <g font-size="2.2" fill="#333"><text x="18" y="76">Negative</text><text x="18" y="108">Positive</text><text x="140" y="76">Negative</text><text x="140" y="108">Positive</text></g>
    <g fill="#0692cd">
      <rect x="38" y="44" width="10" height="52"/><rect x="60" y="44" width="10" height="40"/><rect x="82" y="44" width="10" height="46"/><rect x="104" y="44" width="10" height="50"/>
      <rect x="160" y="44" width="10" height="64"/><rect x="182" y="44" width="10" height="60"/><rect x="204" y="44" width="10" height="62"/><rect x="226" y="44" width="10" height="64"/>
    </g>
    <g fill="#c9c9c9">
      <rect x="38" y="96" width="10" height="16"/><rect x="60" y="84" width="10" height="28"/><rect x="82" y="90" width="10" height="22"/><rect x="104" y="94" width="10" height="18"/>
      <rect x="182" y="104" width="10" height="8"/><rect x="204" y="106" width="10" height="6"/>
    </g>
    <g font-size="2" fill="#555"><text x="38" y="116">Brenlo</text><text x="59" y="116">CDI+X%</text><text x="81" y="116">Index</text><text x="103" y="116">Peers</text><text x="160" y="116">Brenlo</text><text x="181" y="116">CDI+X%</text><text x="203" y="116">Index</text><text x="225" y="116">Peers</text></g>
  </svg>
  <div class="body" style="top:124px;font-size:2.2px;width:236px">From 6 months until 12% in investment windows, 100% were better than benchmark and 94% than peers.</div>
  <div class="page">16</div><div class="brand"><i></i>BRENLO CAPITAL</div>
</section>

<!-- Key facts -->
<section class="slide c1 r5">
  <div class="title">Brenlo Macro Global Fund</div>
  <div class="subtitle">Key Facts</div>
  <div class="page">17</div><div class="brand"><i></i>BRENLO CAPITAL</div>
</section>

<!-- Flagship funds -->
<section class="slide c2 r5">
  <div class="title">Flagship Funds</div>
  <div class="subtitle">Flagship funds, AuM (November 2017), volatility and main asset classes</div>
  <div class="box b-blue" style="left:18px;top:35px;width:55px;height:34px;flex-direction:column">BRENLO / STRATEGY<br>Macro Global Fund – Long Term Focus</div>
  <div class="box b-navy" style="left:77px;top:35px;width:55px;height:34px;flex-direction:column">BRENLO / MACRO<br>Macro fund, long-term trading, rates and currencies</div>
  <div class="box b-grey" style="left:136px;top:35px;width:55px;height:34px;flex-direction:column">BRENLO / ADVANCED<br>A fund with greater leverage</div>
  <div class="box b-dgrey" style="left:195px;top:35px;width:55px;height:34px;flex-direction:column">BRENLO / PREV<br>High-value pension fund with the same philosophy</div>
  <div class="box b-blue" style="left:18px;top:73px;width:55px;height:7px">R$ 2.0 billion (Target)</div>
  <div class="box b-navy" style="left:77px;top:73px;width:55px;height:7px">R$ 1.2 billion (Closed)</div>
  <div class="box b-grey" style="left:136px;top:73px;width:55px;height:7px">R$ 4.0 billion (Closed)</div>
  <div class="box b-dgrey" style="left:195px;top:73px;width:55px;height:7px">R$ 2.1 billion (Open)</div>
  <div class="box b-blue" style="left:18px;top:84px;width:55px;height:7px">Target VOL 10%</div>
  <div class="box b-navy" style="left:77px;top:84px;width:55px;height:7px">Target VOL 8%</div>
  <div class="box b-grey" style="left:136px;top:84px;width:55px;height:7px">Target VOL 18%</div>
  <div class="box b-dgrey" style="left:195px;top:84px;width:55px;height:7px">n/a</div>
  <div class="box b-blue" style="left:18px;top:95px;width:55px;height:30px">Global fixed income, Brazil and global currencies, shares and equity indexes</div>
  <div class="box b-navy" style="left:77px;top:95px;width:55px;height:30px">Brazil fixed income, Global fixed income, Brazil and global currencies</div>
  <div class="box b-grey" style="left:136px;top:95px;width:55px;height:30px">Brazil fixed income, Global fixed income, Local and global stock indices</div>
  <div class="box b-dgrey" style="left:195px;top:95px;width:55px;height:30px">Same investment process as the Macro fund, with a pension wrapper</div>
  <div class="page">18</div><div class="brand"><i></i>BRENLO CAPITAL</div>
</section>

<!-- Flagship performance -->
<section class="slide c3 r5">
  <div class="title">Flagship Funds Performance</div>
  <div class="subtitle" style="font-size:3.4px">Performance: Brenlo Advanced, Brenlo Macro and Prev (pension fund's portfolio)</div>
  <svg width="272" height="153" viewBox="0 0 272 153">
    <g font-size="2.2" fill="#0692cd" text-anchor="middle"><text x="136" y="36">2% ABOVE ADVANCED – Average of CDI (95.98% BR)</text><text x="136" y="68">2% ABOVE MACRO – Average of CDI (98.37% BR)</text><text x="136" y="100">2% ABOVE PREV – Average of CDI (91.24% BR)</text></g>
    <g stroke="#d6d6d6" stroke-width="0.3">
      <line x1="18" y1="39" x2="254" y2="39"/><line x1="18" y1="44" x2="254" y2="44"/><line x1="18" y1="49" x2="254" y2="49"/><line x1="18" y1="54" x2="254" y2="54"/><line x1="18" y1="59" x2="254" y2="59"/>
      <line x1="18" y1="71" x2="254" y2="71"/><line x1="18" y1="76" x2="254" y2="76"/><line x1="18" y1="81" x2="254" y2="81"/><line x1="18" y1="86" x2="254" y2="86"/><line x1="18" y1="91" x2="254" y2="91"/>
      <line x1="18" y1="103" x2="254" y2="103"/><line x1="18" y1="108" x2="254" y2="108"/><line x1="18" y1="113" x2="254" y2="113"/><line x1="18" y1="118" x2="254" y2="118"/><line x1="18" y1="123" x2="254" y2="123"/>
    </g>
    <g font-size="1.9" fill="#555">
      <text x="20" y="42">Jan  Feb  Mar  Apr  May  Jun  Jul  Aug  Sep  Oct  Nov  Dec  Year</text>
      <text x="20" y="47">2014   0.82  1.05  1.21  0.54  1.10  0.98  1.44  0.71  0.66  1.02  0.93  1.15  12.3</text>
      <text x="20" y="52">2015   1.12  0.45  2.07  1.38  0.93  1.01  0.88  1.54  0.79  1.11  1.03  0.92  14.1</text>
      <text x="20" y="57">2016   1.25  1.09  0.97  1.61  1.02  0.87  1.33  1.08  0.95  1.18  0.84  1.07  15.0</text>
      <text x="20" y="74">Jan  Feb  Mar  Apr  May  Jun  Jul  Aug  Sep  Oct  Nov  Dec  Year</text>
      <text x="20" y="79">2014   0.71  0.94  1.02  0.48  0.99  0.87  1.21  0.66  0.59  0.93  0.85  1.04  11.2</text>
      <text x="20" y="84">2015   1.03  0.41  1.77  1.22  0.86  0.92  0.81  1.38  0.71  1.02  0.96  0.85  12.9</text>
      <text x="20" y="89">2016   1.14  0.99  0.90  1.45  0.94  0.80  1.21  0.99  0.88  1.07  0.78  0.98  13.6</text>
      <text x="20" y="106">Jan  Feb  Mar  Apr  May  Jun  Jul  Aug  Sep  Oct  Nov  Dec  Year</text>
      <text x="20" y="111">2015   0.66  0.38  1.41  1.02  0.77  0.83  0.74  1.19  0.65  0.91  0.87  0.79  10.8</text>
      <text x="20" y="116">2016   0.98  0.87  0.82  1.26  0.85  0.74  1.08  0.90  0.81  0.97  0.71  0.89  11.9</text>
      <text x="20" y="121">2017   0.92  0.81  0.77  1.12  0.80  0.70  1.01  0.84  0.76  0.90  0.67  0.83  10.6</text>
    </g>
    <text x="18" y="131" font-size="2" fill="#888">Source: Brenlo Capital; past performance is no guarantee</text>
  </svg>
  <div class="page">19</div><div class="brand"><i></i>BRENLO CAPITAL</div>
</section>

<!-- Team -->
<section class="slide c4 r5">
  <div class="title">The Team</div>
  <svg width="272" height="153" viewBox="0 0 272 153">
    <g font-size="2.2" fill="#555"><text x="90" y="40">1999</text><text x="113" y="40">2004</text><text x="136" y="40">2005</text><text x="159" y="40">2008</text><text x="182" y="40">2009</text><text x="205" y="40">2010</text><text x="228" y="40">2015</text><text x="246" y="40">2017</text></g>
    <g font-size="2" fill="#0692cd">
      <text x="18" y="47">Tomas Varel</text><text x="18" y="52">CIO</text><text x="18" y="67">Trader</text><text x="18" y="72">Economist</text><text x="18" y="77">Analyst</text><text x="18" y="82">Risk Officer</text><text x="18" y="87">Portfolio Mgr</text><text x="18" y="92">Strategist</text><text x="18" y="97">Quant</text><text x="18" y="102">Analyst</text>
      <text x="18" y="62">Partner B</text>
    </g>
    <g font-size="2" fill="#777"><text x="18" y="114">Compliance</text><text x="18" y="120">Middle Office</text><text x="18" y="126">Legal</text><text x="18" y="132">Admin</text></g>
    <g fill="#0692cd">
      <rect x="105" y="44" width="150" height="3.5"/><rect x="120" y="49" width="135" height="3.5"/><rect x="18" y="54" width="237" height="3.5" fill="#0255a3"/>
      <rect x="140" y="59" width="115" height="3.5"/><rect x="150" y="64" width="105" height="3.5" fill="#0255a3"/><rect x="160" y="69" width="95" height="3.5"/>
      <rect x="175" y="74" width="80" height="3.5"/><rect x="185" y="79" width="70" height="3.5"/><rect x="200" y="84" width="55" height="3.5" fill="#0255a3"/>
      <rect x="210" y="89" width="45" height="3.5"/><rect x="225" y="94" width="30" height="3.5"/><rect x="235" y="99" width="20" height="3.5"/>
    </g>
    <g fill="#b5b5b5">
      <rect x="18" y="104" width="237" height="3.5"/><rect x="150" y="110" width="105" height="3.5"/><rect x="175" y="116" width="80" height="3.5"/><rect x="205" y="122" width="50" height="3.5"/><rect x="225" y="128" width="30" height="3.5"/>
    </g>
  </svg>
  <div class="page">20</div><div class="brand"><i></i>BRENLO CAPITAL</div>
</section>

<!-- Disclosures -->
<section class="slide c2 r6">
  <div class="title">Disclosures</div>
  <div class="page">21</div><div class="brand"><i></i>BRENLO CAPITAL</div>
</section>

<!-- Contact -->
<section class="slide c3 r6">
  <div class="title">Contact information</div>
  <div class="page">22</div><div class="brand"><i></i>BRENLO CAPITAL</div>
</section>

</div>
</body>
</html>
```